Laminated Training Card; highly professional yet engaging, colorful, fits branding

We need an 8 1/2" x 11" piece, printed front and back, to inspire and offer instructions for nonprofit leaders on key coaching skills to use with their staff. Though it's in a professional services setting, this piece communicates a sense of fun and excitement to encourage leaders to try out these skills, and keep the training card close at hand. An infographic style would be ideal.

Target Market(s)

Nonprofit leaders will use the laminated training card in a face to face training class, and then take it back to the office to use to 'train' their staff

Industry/Entity Type

Training

Font styles to use
Serif

Requirements
Must have
• See project brief attached
Nice to have
Should not have

```html
<!DOCTYPE html>
<html lang="en">
<head>
<meta charset="utf-8">
<title>Coaching Skills Training Card</title>
<link rel="stylesheet" href="https://fonts.googleapis.com/css2?family=Tinos:ital,wght@0,700;1,700&display=swap">
<style>
  :root {
    --canvas: #e6e6e6;
    --orange: #dd5429;
    --sky: #8dcfe3;
    --lime: #aebd36;
    --pale-sky: #aedfee;
    --ink: #231f20;
    --white: #ffffff;
    --dot: #aebd36;
  }
  * { margin: 0; padding: 0; box-sizing: border-box; }
  html, body { width: 927px; height: 1200px; overflow: hidden; }
  body {
    background: var(--canvas);
    font-family: "Tinos", "Times New Roman", serif;
    font-weight: 700;
    position: relative;
  }
  .band { position: absolute; }
  .band--brag { left: 55px; top: 22px; width: 872px; height: 318px; background: var(--orange); border-radius: 150px 0 0 150px; }
  .band--charter { left: 0; top: 355px; width: 870px; height: 317px; background: var(--sky); border-radius: 0 150px 150px 0; }
  .band--mindful { left: 55px; top: 687px; width: 872px; height: 316px; background: var(--lime); border-radius: 150px 0 0 150px; }
  .band--sources { left: 0; top: 1018px; width: 927px; height: 182px; background: var(--pale-sky); }

  .badge {
    position: absolute; width: 146px; height: 146px; border-radius: 50%;
    background: var(--ink);
  }
  .badge--brag { left: 77px; top: 44px; }
  .badge--charter { left: 702px; top: 397px; }
  .badge--mindful { left: 77px; top: 702px; }

  .section-title {
    position: absolute; font-size: 27px; color: var(--ink);
    width: 400px; text-align: center; line-height: 32px;
  }
  .section-title--brag { left: 264px; top: 41px; }
  .section-title--charter { left: 268px; top: 372px; }
  .section-title--mindful { left: 263px; top: 711px; }

  .copy { position: absolute; color: var(--white); font-size: 18px; line-height: 22.5px; white-space: nowrap; }
  .copy--brag { left: 285px; top: 98px; }
  .copy--brag .quotes { margin-top: 6px; font-style: italic; }
  .copy--charter { left: 52px; top: 438px; }
  .copy--charter p + p { margin-top: 22.5px; }

  .benefits { position: absolute; left: 288px; top: 775px; list-style: none; color: var(--white); font-size: 18px; line-height: 22px; }
  .benefits li { height: 43.5px; }

  .sources-title { position: absolute; top: 1029px; width: 927px; text-align: center; font-size: 17px; color: var(--ink); }
  .sources-list { position: absolute; top: 1085px; width: 927px; list-style: none; text-align: center; font-size: 16.5px; line-height: 21px; color: var(--ink); }
  .sources-list li { height: 21px; }
  .sources-list li::before {
    content: ""; display: inline-block; width: 7px; height: 7px; border-radius: 50%;
    background: var(--dot); margin-right: 6px; vertical-align: 2px;
  }
</style>
</head>
<body>
  <div class="band band--brag"></div>
  <div class="band band--charter"></div>
  <div class="band band--mindful"></div>
  <div class="band band--sources"></div>

  <div class="badge badge--brag" role="img" aria-label="Icon of two team members exchanging praise"></div>
  <div class="badge badge--charter" role="img" aria-label="Icon of a group of three team members"></div>
  <div class="badge badge--mindful" role="img" aria-label="Icon of a team member with a plus sign"></div>

  <h2 class="section-title section-title--brag">#4. Brag Bites</h2>
  <div class="copy copy--brag">
    <p>Brag on the team. Stay away from generalizations; ‘I have a great team’.<br>
    Instead name a value you honored, an obstacle overcome, or what others<br>
    count on. Have 10 team brag bites in your brag bag ready at all times.</p>
    <p class="quotes">‘We fell short of the goal. But we never gave up.’<br>
    ‘We didn’t expect the new people to step up so quickly. We set aside egos<br>
    and followed whoever had the best idea.’<br>
    ‘The whole organization counted on our team’s optimism and hopefulness.’</p>
  </div>

  <h2 class="section-title section-title--charter">#5. Team Charter</h2>
  <div class="copy copy--charter">
    <p>Teams don’t find their focus from the mission statement. It’s too broad,<br>
    vague and doesn’t answer the question: What is our team’s unique<br>
    contribution to achieving the mission? Your &nbsp;answer is your Team Charter.<br>
    Name your values, what’s your impact, how you celebrate success, even what<br>
    you do when things go wrong.</p>
    <p>The Charters answers the questions: if we weren’t here, what would be missing?<br>
    What do we want people to count on from us?</p>
  </div>

  <h2 class="section-title section-title--mindful">#6. &nbsp;Mindfulness</h2>
  <ul class="benefits">
    <li>Improve productivity</li>
    <li>Speed decision making</li>
    <li>Reduce stress and compassion fatigue</li>
    <li>Have more fun and fulfillment</li>
    <li>Build trust</li>
  </ul>

  <h3 class="sources-title">SOURCES</h3>
  <ul class="sources-list">
    <li>‘Speaking Up for the Work You Do’ by Nora Whitfield</li>
    <li>Unfolding by (need to fill this in)</li>
    <li>Leadership Coaching Academy (LCA): 4-Dimensional Leadership Model</li>
    <li>Levels of Focus: Martin Avery &amp; LCA</li>
  </ul>
</body>
</html>
```